International IT Business Needs a Proffesional and Innovative Business Card

We need a proffesional and innovative business card for a new company based in Venezuela called 'KorvaniLink'. We are QTB Business Partner, QTB is a key manufacture for us, one of the most influential players in technology, and the leader in cloud computing, virtualization, Big Data storage and analytics, and IT security and protection.

QTB has developed a global network of business partners to bring customers the full complement of skills and expertise required to build their information infrastructures. This partner ecosystem helps customers maximize the value of their information at the lowest total cost.

We would like to see designs that use the QTB Business Partnet logo & KorvaniLink logo.

http://brand.qtb-example.com/BrandGuide/partners/qtb-business-partner-logo/

Thank you in advance for your interest.
Updates

Happy Day!!!! I look forward to your creative design!!!

Thank you in advance.

Morna Quiroga

Target Market(s)

KorvaniLink's target markets include large companies and small- and medium-sized businesses across various vertical markets.

Industry/Entity Type

Security

Font styles to use
Other font styles liked:
• We use Meta as the QTB® corporate font.

Colors

Designer to choose colors to be used in the design.

Requirements
Must have
• Name
Title
Address
web page (www.korvani.example)

Nice to have
• Add a QR code on the reverse of the card.

```html
<!DOCTYPE html>
<html lang="en">
<head>
<meta charset="utf-8">
<title>KorvaniLink Business Card</title>
<link href="https://fonts.googleapis.com/css2?family=Open+Sans:wght@400;600;700&display=swap" rel="stylesheet">
<style>
  :root {
    --bg: #c9c9cb;
    --paper: #f4f4f3;
    --navy: #2f2a6e;
    --navy-text: #2d2f6b;
    --green: #3cae3f;
    --green-light: #6cc23c;
    --stripe: #d5d5d5;
    --ink-light: #e9e9f2;
    --accent: #8dd23a;
    --muted: #6a6c85;
  }
  * { box-sizing: border-box; margin: 0; padding: 0; }
  html, body { width: 1200px; height: 880px; overflow: hidden; }
  body {
    background: var(--bg);
    font-family: "Open Sans", Arial, sans-serif;
    position: relative;
  }
  .card {
    position: absolute;
    top: 290px;
    width: 520px;
    height: 298px;
    background: var(--paper);
    overflow: hidden;
    box-shadow: 0 10px 24px rgba(0,0,0,0.18);
  }
  .card--front { left: 60px; }
  .card--back { left: 620px; }

  .brand {
    position: absolute;
    display: flex;
    align-items: center;
    gap: 8px;
    color: var(--navy-text);
    font-weight: 700;
  }
  .brand__dot {
    width: 14px; height: 14px; border-radius: 50%;
    background: var(--green);
  }
  .card--front .brand { left: 40px; top: 46px; font-size: 28px; }

  .holder {
    position: absolute;
    right: 28px; top: 50px;
    text-align: right;
    color: var(--navy-text);
  }
  .holder__name { font-size: 17px; font-weight: 700; line-height: 1.3; }
  .holder__title { font-size: 11px; font-weight: 600; color: var(--green); letter-spacing: 0.04em; line-height: 1.6; }

  .contact-band {
    position: absolute;
    left: 0; top: 140px;
    width: 100%; height: 84px;
    background: var(--navy);
    display: flex;
    justify-content: space-between;
    padding: 18px 28px 0 40px;
    color: var(--ink-light);
    font-size: 11px;
    line-height: 1.65;
  }
  .contact-group { display: flex; flex-direction: column; }
  .contact-line { display: flex; align-items: center; gap: 7px; white-space: nowrap; }
  .contact-line svg { width: 11px; height: 11px; flex: none; }
  .contact-line--cont { padding-left: 18px; }
  .separator {
    position: absolute; left: 0; width: 100%;
    height: 8px;
    background: repeating-linear-gradient(135deg, var(--stripe) 0 2px, #ececec 2px 4px);
  }
  .card--front .separator { top: 224px; }
  .green-band {
    position: absolute; left: 0; width: 100%;
    background: linear-gradient(90deg, var(--green) 0%, var(--green-light) 100%);
  }
  .card--front .green-band { top: 232px; bottom: 0; }

  .card--back .brand {
    left: 0; right: 0; top: 104px;
    justify-content: center;
    font-size: 38px;
  }
  .card--back .brand__dot { width: 18px; height: 18px; }
  .card--back .separator { top: 254px; }
  .card--back .green-band { top: 262px; bottom: 0; background: var(--green); }
</style>
</head>
<body>

<section class="card card--front" aria-label="Business card front">
  <div class="brand"><span class="brand__dot"></span><span class="brand__name">KorvaniLink</span></div>

  <div class="holder">
    <p class="holder__name">Morna Quiroga</p>
    <p class="holder__title">Managing Director</p>
  </div>

  <div class="contact-band">
    <div class="contact-group">
      <div class="contact-line">
        <svg viewBox="0 0 12 12"><path d="M6 0.5a3.8 3.8 0 0 0-3.8 3.8C2.2 7.2 6 11.5 6 11.5s3.8-4.3 3.8-7.2A3.8 3.8 0 0 0 6 .5zm0 5.2a1.4 1.4 0 1 1 0-2.8 1.4 1.4 0 0 1 0 2.8z" fill="var(--accent)"/></svg>
        <span>48 Avenida Orinoco,</span>
      </div>
      <div class="contact-line contact-line--cont">Valera TR 3102</div>
    </div>
    <div class="contact-group">
      <div class="contact-line">
        <svg viewBox="0 0 12 12"><path d="M3 1l2 2.5-1.2 1.3c.6 1.4 1.7 2.5 3.1 3.1L8.2 6.7 10.7 8.7 9.4 10.8C5 10.5 1.5 7 1.2 2.6z" fill="var(--accent)"/></svg>
        <span>+58 271 555 0142</span>
      </div>
      <div class="contact-line">
        <svg viewBox="0 0 12 12"><rect x="1.5" y="5" width="9" height="6" fill="var(--accent)"/><rect x="3" y="1" width="6" height="4" fill="none" stroke="var(--accent)" stroke-width="1.2"/></svg>
        <span>+58 271 555 0143</span>
      </div>
    </div>
    <div class="contact-group">
      <div class="contact-line">
        <svg viewBox="0 0 12 12"><circle cx="6" cy="6" r="5" fill="none" stroke="var(--accent)" stroke-width="1.2"/><path d="M1 6h10M6 1c-2 2.7-2 7.3 0 10M6 1c2 2.7 2 7.3 0 10" fill="none" stroke="var(--accent)" stroke-width="1"/></svg>
        <span>www.korvani.example</span>
      </div>
      <div class="contact-line">
        <svg viewBox="0 0 12 12"><rect x="1" y="2.5" width="10" height="7" fill="none" stroke="var(--accent)" stroke-width="1.2"/><path d="M1 2.5l5 4 5-4" fill="none" stroke="var(--accent)" stroke-width="1.2"/></svg>
        <span>morna.quiroga@korvani.example</span>
      </div>
    </div>
  </div>
  <div class="separator"></div>
  <div class="green-band"></div>
</section>

<section class="card card--back" aria-label="Business card back">
  <div class="brand"><span class="brand__dot"></span><span class="brand__name">KorvaniLink</span></div>
  <div class="separator"></div>
  <div class="green-band"></div>
</section>

</body>
</html>
```